A Dance among Quiet Stars

I want the title to look like it’s painted with a paintbrush. This is also a story about my relationship with a spirit of a famous Venetian painter from the 1800s so paint references and swirls are encouraged. The story takes place in Chicago; Bali; Venice, Italy; Sedona, Arizona; and Paris, France. Venice is the most important place. I attached a photo that may make a good cover photo

Target Market(s)

For those interested in travel, spirituality, healing

Requirements
Must have
• The title should look like it’s painted and be flowy
Nice to have
• Story takes place in Venice Italy. Any Venice symbolism would be great

```html
<!DOCTYPE html>
<html lang="en">
<head>
<meta charset="utf-8">
<title>A Dance among Quiet Stars — Book Cover</title>
<link rel="stylesheet" href="https://fonts.googleapis.com/css2?family=Kaushan+Script&display=swap">
<style>
  :root {
    --backdrop: #003366;
    --title-ink: #0e3a78;
    --sky-top: #ffc107;
    --sky-mid: #f79a1a;
    --sky-low: #f26a24;
    --sun-core: #fff3a6;
    --sun-edge: #fde24a;
  }
  * { margin: 0; padding: 0; box-sizing: border-box; }
  html, body {
    width: 1200px;
    height: 1000px;
    overflow: hidden;
    background: var(--backdrop);
  }
  .canvas {
    position: relative;
    width: 1200px;
    height: 1000px;
    background: var(--backdrop);
  }
  .book-cover {
    position: absolute;
    left: 328px;
    top: 81px;
    width: 545px;
    height: 838px;
    overflow: hidden;
    background:
      radial-gradient(ellipse 320px 200px at 50% 0%, var(--sky-top) 0%, rgba(255,193,7,0) 100%),
      linear-gradient(180deg, var(--sky-mid) 0%, #f58a1d 45%, var(--sky-low) 75%, var(--sky-low) 100%);
  }
  .book-title {
    position: absolute;
    top: 92px;
    left: 0;
    width: 100%;
    text-align: center;
    font-family: "Kaushan Script", cursive;
    color: var(--title-ink);
    line-height: 1;
    transform: rotate(-3deg);
  }
  .book-title .line {
    display: block;
    font-size: 84px;
    letter-spacing: -1px;
  }
  .book-title .line--first { margin-left: -20px; }
  .book-title .line--second { margin-top: -6px; margin-left: 30px; font-size: 80px; }
  .book-title .line--second .small { font-size: 52px; }
  .book-title .line--third { margin-top: -4px; margin-left: -10px; }
  .cover-scene {
    position: absolute;
    left: 40px;
    top: 365px;
    width: 470px;
    height: 450px;
    border-radius: 50% 50% 40% 40%;
    background:
      radial-gradient(circle 150px at 50% 33%, var(--sun-core) 0%, var(--sun-edge) 85%, rgba(253,226,74,0) 100%),
      radial-gradient(ellipse 130px 80px at 50% 82%, rgba(253,226,74,0.85) 0%, rgba(253,226,74,0) 100%);
  }
</style>
</head>
<body>
  <main class="canvas">
    <section class="book-cover">
      <h1 class="book-title">
        <span class="line line--first">A Dance</span>
        <span class="line line--second"><span class="small">among</span> Quiet</span>
        <span class="line line--third">Stars</span>
      </h1>
      <div class="cover-scene" role="img" aria-label="Illustration: a large setting sun over water with a gondola in silhouette, a gondolier rowing and a passenger holding a parasol, reflected on the rippling water"></div>
    </section>
  </main>
</body>
</html>
```